Design a Flat design copy of this flyer

Copy the brochure but use flat design instead of 3D.
Copy placement of items.

Winning designer will be awarded website development work for word press site.

```html
<!DOCTYPE html>
<html lang="en">
<head>
<meta charset="utf-8">
<title>Corvan – Integration and Development</title>
<link rel="stylesheet" href="https://fonts.googleapis.com/css2?family=Encode+Sans+Condensed:wght@400;700&family=Roboto+Condensed:wght@400;700&family=Roboto:wght@400;700;900&display=swap">
<style>
  :root {
    --page: #ffffff;
    --panel: #5878a6;
    --panel-dark: #1e1e22;
    --bubble: #ffffff;
    --ink: #333333;
    --ink-soft: #777777;
    --bullet: #2e5a1c;
    --accent-red: #c8171d;
    --accent-yellow: #f2b931;
    --accent-sky: #74a9cf;
    --divider: #a9bcd6;
  }
  * { box-sizing: border-box; margin: 0; padding: 0; }
  html, body { width: 1200px; height: 1000px; overflow: hidden; background: var(--page); }
  .flyer { position: relative; width: 1200px; height: 1000px; background: var(--page); }
  .panel {
    position: absolute; left: 22px; top: 30px; width: 1154px; height: 942px;
    background: linear-gradient(to bottom, var(--panel) 0, var(--panel) 810px, var(--panel-dark) 942px);
  }
  .brand {
    position: absolute; left: 68px; top: 104px; display: flex; align-items: center; gap: 10px;
  }
  .brand-square { width: 26px; height: 26px; background: var(--accent-sky); }
  .brand-name {
    font-family: "Encode Sans Condensed", sans-serif; font-weight: 700; font-size: 30px; color: #ffffff;
  }
  .services {
    position: absolute; left: 232px; top: 100px; display: flex; list-style: none; white-space: nowrap;
    font-family: "Encode Sans Condensed", sans-serif; font-size: 37px; color: #ffffff; line-height: 48px;
    letter-spacing: 0.4px;
  }
  .services li { padding: 0 4px; }
  .services li:first-child { padding-left: 0; }
  .services li + li { border-left: 2px solid var(--divider); }
  .bubbles { position: absolute; left: 0; top: 0; }
  .copy {
    position: absolute; list-style: none;
    font-family: "Roboto Condensed", sans-serif; font-size: 20px; color: var(--ink); line-height: 34px;
  }
  .copy li { position: relative; padding-left: 24px; }
  .copy li::before {
    content: "•"; position: absolute; left: 8px; color: var(--bullet); font-weight: 700;
  }
  .copy b { font-weight: 700; }
  .copy .initial { color: var(--accent-red); }
  .copy-features { left: 70px; top: 248px; width: 560px; letter-spacing: 0.3px; }
  .copy-access { left: 768px; top: 236px; width: 360px; line-height: 36px; letter-spacing: 0.3px; }
  .product-name {
    position: absolute; left: 790px; top: 560px; white-space: nowrap;
    font-family: "Roboto", sans-serif; font-weight: 900; font-size: 80px; color: var(--accent-yellow);
    line-height: 1;
  }
  .tagline {
    position: absolute; left: 69px; top: 752px; width: 1059px; text-align: center;
    font-family: "Roboto Condensed", sans-serif; font-size: 28px; color: var(--ink-soft); letter-spacing: 0.4px;
  }
  .tagline b { font-weight: 700; }
</style>
</head>
<body>
<main class="flyer">
  <div class="panel"></div>

  <div class="brand">
    <span class="brand-square"></span>
    <span class="brand-name">Corvan</span>
  </div>

  <ul class="services">
    <li>NoSQL</li><li>Glass</li><li>Watch</li><li>DDSB</li><li>SMS</li><li>Red Beam</li><li>OCR</li><li>Speech to Text</li>
  </ul>

  <svg class="bubbles" width="1200" height="1000" viewBox="0 0 1200 1000" aria-hidden="true">
    <polygon fill="var(--bubble)" points="69,225 650,225 650,560 612,516 69,516"/>
    <polygon fill="var(--bubble)" points="755,230 1130,230 1130,432 1095,386 755,386"/>
    <polygon fill="var(--bubble)" points="69,728 1128,728 1128,852 1090,808 69,808"/>
  </svg>

  <ul class="copy copy-features">
    <li>Use our <b>D</b>rag &amp; <b>D</b>rop <b>S</b>creen <b>B</b>uilder to quickly create your<br>own system, or pick from our available business teamplates.</li>
    <li>Customise to your specific needs.</li>
    <li>Integrate with Providers &amp; Suppliers using our API bank, if<br>the API isn’t available, then we will build it!</li>
    <li>React to market changes. You can change the business<br>rules, work flow or data management, you are in control.</li>
  </ul>

  <ul class="copy copy-access">
    <li>Accessible from Desktop,<br>Tablet &amp; Mobile with your own app</li>
    <li>Energy Efficient</li>
    <li><span class="initial">F</span>lexible <span class="initial">E</span>ntity <span class="initial">L</span>inking</li>
  </ul>

  <div class="product-name">VANTREL</div>

  <p class="tagline"><b>Integration and Development made easy</b>. Create your software that works for you!</p>
</main>
</body>
</html>
```